Corporate Business Card

Very professional, Modern, Not to busy, include phone address email, website
(253) 555-0174, 61807 19th Street N, Kent, WA 98517, marcus@kestrelbayholding.com, brelvanindustries.com

Target Market(s)

Manufacturing

Industry/Entity Type

Aero, machining, manufacturing, Off road racing

Contact Information for Business Card

Phone, address email, website

```html
<!DOCTYPE html>
<html lang="en">
<head>
<meta charset="utf-8">
<title>Brelvan Industries – Business Card</title>
<link rel="stylesheet" href="https://fonts.googleapis.com/css2?family=Orbitron:wght@500;700&display=swap">
<style>
  :root {
    --backdrop: #cddcf1;
    --card: #ffffff;
    --navy: #14336b;
    --red: #d42429;
    --ink-light: #ffffff;
  }
  * { margin: 0; padding: 0; box-sizing: border-box; }
  html, body {
    width: 1200px; height: 1200px; overflow: hidden;
    background: var(--backdrop);
    font-family: "Orbitron", sans-serif;
    color: var(--navy);
  }
  .card {
    position: absolute;
    left: 371px;
    width: 459px;
    height: 276px;
    background: var(--card);
  }
  .card--front { top: 247px; }
  .card--back { top: 684px; }

  .brand {
    display: flex;
    align-items: center;
    gap: 8px;
    font-weight: 700;
    color: var(--navy);
    letter-spacing: 0.02em;
    white-space: nowrap;
  }
  .brand__mark {
    background: var(--navy);
    flex: none;
  }
  .card--front .brand {
    position: absolute;
    left: 0; right: 0; top: 104px;
    justify-content: center;
    font-size: 22px;
  }
  .card--front .brand__mark { width: 16px; height: 16px; }

  .front__web {
    position: absolute;
    left: 0; right: 0; top: 234px;
    text-align: center;
    font-size: 7.5px;
    font-weight: 500;
    letter-spacing: 0.03em;
  }

  .card--back .brand {
    position: absolute;
    left: 31px; top: 34px;
    font-size: 12px;
    gap: 6px;
  }
  .card--back .brand__mark { width: 10px; height: 10px; }

  .person { position: absolute; left: 31px; top: 122px; }
  .person__name {
    font-size: 19px;
    font-weight: 700;
    letter-spacing: 0.04em;
    line-height: 1;
  }
  .person__title {
    margin-top: 3px;
    font-size: 10px;
    font-weight: 500;
    font-style: italic;
    letter-spacing: 0.03em;
  }

  .contact-band {
    position: absolute;
    left: 0; bottom: 0;
    width: 432px; height: 95px;
    background: var(--navy);
    clip-path: polygon(0 0, 100% 0, 77.3% 100%, 0 100%);
    color: var(--ink-light);
    font-size: 8px;
    font-weight: 500;
    letter-spacing: 0.03em;
    line-height: 12.2px;
  }
  .contact-band__address { position: absolute; left: 30px; top: 29px; }
  .contact-band__lines {
    position: absolute; left: 181px; top: 29px;
    display: grid;
    grid-template-columns: 33px auto;
  }
</style>
</head>
<body>
  <section class="card card--front">
    <div class="brand"><span class="brand__mark"></span>Brelvan Industries</div>
    <p class="front__web">www.brelvanindustries.com</p>
  </section>

  <section class="card card--back">
    <div class="brand"><span class="brand__mark"></span>Brelvan Industries</div>
    <div class="person">
      <h1 class="person__name">MARCUS ORLEN</h1>
      <p class="person__title">Chief Executive Officer</p>
    </div>
    <div class="contact-band">
      <p class="contact-band__address">61807 19th Street N,<br>Kent, WA 98517</p>
      <div class="contact-band__lines">
        <span>Mob</span><span>(253) 555-0174</span>
        <span>Mail</span><span>marcus@kestrelbayholding.com</span>
        <span>Web</span><span>www.brelvanindustries.com</span>
      </div>
    </div>
  </section>
</body>
</html>
```